RM Tomás Rivera (Business Card)

Hi designers, in this work, I'm looking for an sophisticated stylish, elegant and proffesional personal card. We have a laboratory of pathology automated, with equipments high quality.
In this web the designers, have created my business logo, the name is "RM Tomás Rivera"
In our lab, we principal work is to prepare the biopsies for further diagnostic of diseases like cancer, tumors, etc.
I need that the first face, only having my complete logo (Rm Tomás Rivera, Laboratorio de procesamiento Histologico)
The overleaf, could repeat the same logo, like water logo.
In this face, I need to say: My full data:

Técnico en Anatomía Patológica
Tomás Rivera Ibarra M.P 47203
Av. Paredes Luján 418 - 2do piso - Instituto Marbel.
Córdoba, Argentina
(0351) 154820937
rivera.tomas@correolab.example

with respect the colors of card, use your imagination, the original logo color is violet, I haven't chosen a color base for the card.

attached pictures are examples of cards I like your DESIGN.
Attached too, the original logo to my company.

the size of card are:
horizontal: 9cm
vertical: 5,5cm

any question that you have, not doubt to question me,
Hand to work!

Industry/Entity Type

Laboratory

Requirements
Must have
• designers sophisticated, not simples, like show the images attached

```html
<!DOCTYPE html>
<html lang="es">
<head>
<meta charset="utf-8">
<title>Tomás Rivera — Tarjeta personal</title>
<link rel="stylesheet" href="https://fonts.googleapis.com/css2?family=Arimo:wght@700&family=Ubuntu:wght@400&family=Roboto+Condensed:wght@400&family=Raleway:wght@400&display=swap">
<style>
  :root {
    --backdrop: #2b2b2d;
    --card-white: #f3f3f3;
    --violet: #6b2f8a;
    --violet-deep: #5d2679;
    --violet-light: #7a3b98;
    --grey-swoosh: #8c8c8c;
    --ink: #2e2e2e;
    --ink-soft: #3a3a3a;
    --on-violet: #f1ecf4;
  }
  * { margin: 0; padding: 0; box-sizing: border-box; }
  html, body { width: 1200px; height: 900px; overflow: hidden; }
  body { background: var(--backdrop); position: relative; font-family: "Ubuntu", sans-serif; }

  .card { position: absolute; left: 370px; width: 456px; height: 278px; overflow: hidden; }

  /* Front: personal data */
  .card--front { top: 161px; background: var(--card-white); }
  .front__tab { position: absolute; left: 0; top: 250px; width: 16px; height: 27px;
    background: var(--violet); border-radius: 0 5px 5px 0; top: 89px; }
  .front__name { position: absolute; left: 27px; top: 85px; font-family: "Arimo", sans-serif;
    font-weight: 700; font-size: 16.5px; color: var(--ink); }
  .front__licence { position: absolute; left: 27px; top: 106px; font-size: 11.5px; color: var(--violet); }

  .brand { position: absolute; display: flex; flex-direction: column; align-items: center; }
  .brand__mark { width: 34px; height: 34px; background: var(--violet); }
  .brand__name { font-family: "Raleway", sans-serif; font-weight: 400; letter-spacing: 3.5px;
    text-transform: uppercase; white-space: nowrap; }
  .card--front .brand { left: 232px; top: 38px; width: 212px; }
  .card--front .brand__mark { margin-bottom: 14px; }
  .card--front .brand__name { font-size: 12px; color: var(--violet); }

  .contact { position: absolute; left: 28px; top: 172px; list-style: none; }
  .contact li { display: flex; align-items: center; height: 15px; font-size: 11.5px; color: var(--ink-soft); }
  .contact svg { width: 11px; height: 11px; margin-right: 12px; fill: var(--violet); }

  .office { position: absolute; left: 234px; top: 172px; list-style: none; }
  .office li { height: 15px; line-height: 15px; font-size: 11.5px; color: var(--ink-soft); }

  .front__waves { position: absolute; left: 0; bottom: 0; width: 456px; height: 60px; }

  /* Back: laboratory identity */
  .card--back { top: 471px;
    background: linear-gradient(160deg, var(--violet-light) 0%, var(--violet) 45%, var(--violet-deep) 100%); }
  .card--back .brand { left: 0; top: 94px; width: 456px; }
  .card--back .brand__mark { width: 40px; height: 40px; background: var(--on-violet); margin-bottom: 14px; }
  .card--back .brand__name { font-size: 12.5px; color: var(--on-violet); }
  .brand__rule { width: 220px; height: 1px; background: var(--on-violet); margin-top: 3px; }
  .brand__tagline { margin-top: 6px; font-family: "Roboto Condensed", sans-serif; font-size: 15.5px;
    color: var(--on-violet); text-transform: uppercase; white-space: nowrap; }
</style>
</head>
<body>

<section class="card card--front" aria-label="Tarjeta, frente con datos personales">
  <span class="front__tab"></span>
  <h1 class="front__name">Tomás Rivera Ibarra</h1>
  <p class="front__licence">M.P. 47203</p>

  <div class="brand">
    <span class="brand__mark"></span>
    <span class="brand__name">Tomás Rivera</span>
  </div>

  <ul class="contact">
    <li>
      <svg viewBox="0 0 12 12" aria-hidden="true"><path d="M2.4 1 4.3 3.4 3.4 4.6c.8 1.6 2 2.8 3.9 3.9l1.2-.9L11 9.5 9.9 11C5.2 10.4 1.6 6.8 1 2.1z"/></svg>
      (0351) 154820937
    </li>
    <li>
      <svg viewBox="0 0 12 12" aria-hidden="true"><path d="M1 3h10v7H1zM1.8 3.6 6 6.9l4.2-3.3v.9L6 7.8 1.8 4.5z" fill-rule="evenodd"/></svg>
      rivera.tomas@correolab.example
    </li>
    <li>
      <svg viewBox="0 0 12 12" aria-hidden="true"><path d="M6 1a5 5 0 1 0 0 10A5 5 0 0 0 6 1zm0 1c.7.7 1.2 1.9 1.3 3.5H4.7C4.8 3.9 5.3 2.7 6 2zM2.1 5.5a4 4 0 0 1 2.4-3.2c-.5.9-.8 2-.8 3.2zm5.4-3.2a4 4 0 0 1 2.4 3.2H8.3c0-1.2-.3-2.3-.8-3.2zM2.1 6.5h1.6c0 1.2.3 2.3.8 3.2a4 4 0 0 1-2.4-3.2zm2.6 0h2.6C7.2 8.1 6.7 9.3 6 10c-.7-.7-1.2-1.9-1.3-3.5zm3.6 0h1.6a4 4 0 0 1-2.4 3.2c.5-.9.8-2 .8-3.2z"/></svg>
      www.tomas-rivera.example
    </li>
  </ul>

  <ul class="office">
    <li>Técnico en Anatomía Patológica</li>
    <li>Av. Paredes Luján 418 - 2do piso</li>
    <li>Instituto Marbel, Córdoba, Argentina</li>
  </ul>

  <svg class="front__waves" viewBox="0 0 456 60" preserveAspectRatio="none" aria-hidden="true">
    <path d="M0 52 Q120 18 420 14 Q200 16 0 36 Z" fill="var(--grey-swoosh)"/>
    <path d="M0 60 L0 58 Q150 26 300 24 Q400 24 456 30 L456 60 Z" fill="var(--violet)"/>
  </svg>
</section>

<section class="card card--back" aria-label="Tarjeta, dorso con identidad del laboratorio">
  <div class="brand">
    <span class="brand__mark"></span>
    <span class="brand__name">Tomás Rivera</span>
    <span class="brand__rule"></span>
    <span class="brand__tagline">Laboratorio de procesamiento histologico</span>
  </div>
</section>

</body>
</html>
```